Career Counsellor needs vibrant, professional flyer to promote inspiring new webinar

I need a flyer design, A5, double sided. I am a Career Counsellor who helps professionals create fulfilling and inspiring careers and am running a free webinar to promote my program.

I want a design which is simple, elegant and professional with the copy as below. I like dark backgrounds in general (also my name is Wren!!)
I have attached my logo, profile photo and a couple of stock photos to provide an ideal of look/feel (but you can use different stock images if you find something better).

My brand colours are:
Primary - Teal 208FA0
Highlight - Salmon F3745D
with Grey or Wren.

Copy:

(Headline)
Figuring out your next career move is easier than you think...

(webinar details)
FREE WEBINAR
"Why Working Life Can Feel Purposeful Again Using One Simple Weekly Habit Plan"
Weds 3rd Oct 7.30pm (AWST Perth)
Register here: https://zuvrel.link/7kqWzeP

(my profile)
As a Career Counsellor with 14 years of mining industry experience, I’m passionate about helping professionals get inspired by their careers.

(testimonials)
"Ilse is amazing. I am so excited to now have a direction. I have finally found that spark again."
- Corinne Fadley -

"Ilse steered me carefully and faithfully resulting in concrete outcomes with razor sharp clarity for me about how to proceed."
- Margit Ostby -

Target Market(s)

My target audience are mainly professional women, but also men, aged 35-45.

Font styles to use
Sans Serif
Other font styles liked:
• Logo is montserrat extra light

Requirements
Must have
• Copy provided plus profile picture and logo.
• Stylish, creative but simple design.

```html
<!DOCTYPE html>
<html lang="en">
<head>
<meta charset="utf-8">
<title>Flyer Design 02 – Ilse Wren Career Planning Webinar</title>
<link rel="stylesheet" href="https://fonts.googleapis.com/css2?family=Oswald:wght@400;500&family=Montserrat:wght@400;500&family=Source+Sans+3:wght@300;400&display=swap">
<style>
  :root{
    --teal:#16808f;
    --teal-deep:#0f6c7a;
    --teal-light:#1c9fb4;
    --cyan:#3ccbe0;
    --salmon:#f3745d;
    --salmon-soft:#f47d63;
    --navy:#1f2c5f;
    --ink:#151515;
    --white:#ffffff;
    --board-light:#d6d6d6;
    --board-dark:#a9a9a9;
  }
  *{margin:0;padding:0;box-sizing:border-box}
  html,body{width:1200px;height:865px;overflow:hidden}
  body{
    position:relative;
    background:radial-gradient(ellipse at 50% 40%,var(--board-light) 0%,var(--board-dark) 100%);
    font-family:"Montserrat",sans-serif;
  }
  .board-title,.side-label{
    position:absolute;font-family:"Montserrat",sans-serif;font-weight:400;color:var(--ink);
    white-space:nowrap;transform:translateX(-50%);
  }
  .board-title{left:606px;top:12px;font-size:36px;letter-spacing:1px}
  .side-label{top:822px;font-size:34px}
  .side-label--a{left:298px}
  .side-label--b{left:886px}

  .flyer{
    position:absolute;top:98px;width:494px;height:700px;overflow:hidden;
    box-shadow:4px 5px 8px rgba(0,0,0,.35);
  }
  .flyer--front{left:65px;background:linear-gradient(170deg,var(--teal-deep) 0%,var(--teal) 55%,#1a8d9c 100%)}
  .flyer--back{left:644px;background:var(--white)}
  .abs{position:absolute;white-space:nowrap}

  /* brand name */
  .brand{display:flex;align-items:center}
  .brand-dot{border-radius:50%;background:var(--salmon);flex:none}
  .brand-name{font-family:"Montserrat",sans-serif;font-weight:400;line-height:1}

  /* front */
  .front-photo{
    position:absolute;left:230px;top:180px;width:264px;height:520px;
    background:radial-gradient(ellipse at 60% 45%,#6b4a3a 0%,#3b7f8a 45%,rgba(22,128,143,0) 75%),
               linear-gradient(180deg,rgba(22,128,143,0) 0%,#2a95a6 70%,#1f8797 100%);
  }
  .deco-ring{position:absolute;left:-120px;top:420px;width:320px;height:320px;border-radius:50%;background:var(--teal-light);opacity:.75}
  .deco-disc{position:absolute;left:-80px;top:500px;width:340px;height:340px;border-radius:50%;background:var(--salmon-soft)}
  .brand--small{left:300px;top:26px;gap:8px}
  .brand--small .brand-dot{width:20px;height:20px}
  .brand--small .brand-name{font-size:22px;color:var(--white)}
  .kicker{left:27px;top:32px;font-family:"Oswald",sans-serif;font-size:20px;color:var(--white);letter-spacing:.5px}
  .headline-next{left:24px;top:48px;font-family:"Oswald",sans-serif;font-weight:500;font-size:96px;line-height:1;color:var(--cyan);letter-spacing:-2px}
  .headline-career{left:24px;top:136px;font-family:"Oswald",sans-serif;font-weight:500;font-size:96px;line-height:1;color:var(--salmon);letter-spacing:-2px}
  .headline-tail{left:27px;top:234px;font-family:"Oswald",sans-serif;font-size:20px;color:var(--white);letter-spacing:.5px}
  .webinar-topic{left:27px;top:282px;font-family:"Source Sans 3",sans-serif;font-weight:300;font-size:17.5px;line-height:21.6px;color:var(--white);white-space:normal;width:180px}
  .register{left:27px;top:638px;font-family:"Source Sans 3",sans-serif;color:var(--white)}
  .register-label{font-size:19px;font-weight:400;line-height:1.1}
  .register-url{font-size:15px;font-weight:400}
  .webinar-title{right:11px;top:514px;text-align:right;font-family:"Oswald",sans-serif;font-weight:500;color:var(--salmon);font-size:60px;line-height:54px;letter-spacing:2px}
  .webinar-when{right:10px;top:640px;text-align:right;font-family:"Montserrat",sans-serif;font-size:12.5px;line-height:18px;letter-spacing:1.6px;color:var(--white)}

  /* back */
  .back-scenery{
    position:absolute;left:0;top:180px;width:494px;height:520px;
    background:linear-gradient(180deg,rgba(255,255,255,1) 0%,#d9e8dc 18%,#8fbfa6 40%,#3c9a80 62%,#1d6d5c 85%,#174f44 100%);
  }
  .brand--large{left:42px;top:36px;gap:18px}
  .brand--large .brand-dot{width:56px;height:56px}
  .brand--large .brand-name{font-size:50px;color:var(--ink)}
  .profile{left:0;width:494px;top:117px;text-align:center;font-family:"Montserrat",sans-serif;font-size:13px;line-height:18.4px;letter-spacing:1.4px;color:var(--ink)}
  .praise-kicker{left:110px;top:230px;font-family:"Montserrat",sans-serif;font-size:24px;color:var(--salmon);letter-spacing:.3px}
  .praise-word{left:106px;top:258px;font-family:"Montserrat",sans-serif;font-weight:500;font-size:72px;line-height:1;color:var(--salmon);letter-spacing:-2px}
  .quote-band{position:absolute;left:0;width:494px;background:var(--navy)}
  .quote-band--one{top:381px;height:97px}
  .quote-band--two{top:542px;height:99px}
  .quote{font-family:"Montserrat",sans-serif;font-size:11.5px;line-height:16px;letter-spacing:1.2px;color:var(--white)}
  .quote-author{font-family:"Montserrat",sans-serif;font-size:11.5px;letter-spacing:1.2px;color:var(--white)}
  .quote--one{right:198px;top:393px;text-align:right}
  .quote-author--one{right:198px;top:452px}
  .quote--two{left:192px;top:558px}
  .quote-author--two{left:200px;top:615px}
  .portrait{position:absolute;border-radius:50%}
  .portrait--one{left:312px;top:346px;width:164px;height:164px;background:radial-gradient(circle at 50% 45%,#e8c0a6 0%,#c58a5f 40%,#5a3a2a 80%)}
  .portrait--two{left:31px;top:523px;width:138px;height:138px;background:radial-gradient(circle at 50% 45%,#e9c6b1 0%,#9a6446 45%,#e6e6e6 85%);border:2px solid #b9b9b9}
</style>
</head>
<body>
  <h1 class="board-title">FLYER DESIGN 02</h1>

  <section class="flyer flyer--front" aria-label="Flyer side A">
    <div class="front-photo" role="img" aria-label="Photo of a woman in sunglasses and a teal denim shirt, looking up into the wind"></div>
    <div class="deco-ring"></div>
    <div class="deco-disc"></div>

    <div class="abs brand brand--small">
      <span class="brand-dot"></span>
      <span class="brand-name">Ilse Wren</span>
    </div>

    <p class="abs kicker">FIGURING OUT YOUR</p>
    <p class="abs headline-next">NEXT</p>
    <p class="abs headline-career">CAREER</p>
    <p class="abs headline-tail">IS EASIER THAN YOU THINK . . .</p>

    <p class="abs webinar-topic">Why Working Life Can Feel Purposeful Again Using One Simple Weekly Habit Plan</p>

    <div class="abs register">
      <p class="register-label">REGISTER HERE:</p>
      <p class="register-url">https://zuvrel.link/7kqWzeP</p>
    </div>

    <p class="abs webinar-title">FREE<br>WEBINAR</p>
    <p class="abs webinar-when">WEDNESDAY 3RD OCTOBER<br>7.30 PM (AWST PERTH)</p>
  </section>

  <section class="flyer flyer--back" aria-label="Flyer side B">
    <div class="back-scenery" role="img" aria-label="Soft-focus photo of a grass seed head against a green background"></div>

    <div class="abs brand brand--large">
      <span class="brand-dot"></span>
      <span class="brand-name">Ilse Wren</span>
    </div>

    <p class="abs profile">As a Career Counsellor with 14 years of<br>mining industry experience,<br>I’m passionate about helping professionals<br>get inspired by their careers.</p>

    <p class="abs praise-kicker">APPRECIATED BY THE</p>
    <p class="abs praise-word">PEOPLE</p>

    <div class="quote-band quote-band--one"></div>
    <div class="quote-band quote-band--two"></div>

    <p class="abs quote quote--one">"Ilse is amazing. I am so excited to<br>now have a direction. I have finally<br>found that spark again."</p>
    <p class="abs quote-author quote-author--one">-- Corinne Fadley</p>
    <div class="portrait portrait--one" role="img" aria-label="Portrait photo of Corinne Fadley"></div>

    <div class="portrait portrait--two" role="img" aria-label="Portrait photo of Margit Ostby"></div>
    <p class="abs quote quote--two">"Ilse steered me carefully and faithfully<br>resulting in concrete outcomes with razor<br>sharp clarity for me about how to proceed."</p>
    <p class="abs quote-author quote-author--two">-- Margit Ostby</p>
  </section>

  <p class="side-label side-label--a">SIDE A</p>
  <p class="side-label side-label--b">SIDE B</p>
</body>
</html>
```